Motivationskarten für Trainer und Coach
Zielgruppe
Ich bin Trainer und Coach mit Schwerpunkt Effizienz/ Zeit- und Selbstmanagement sowie Büroorganisation. Meine Kunden buchen bei mir Seminare, um Ihren Arbeitsalltag effizienter zu gestalten und zu strukturieren und Ihre Büroabläufe sowie Prozesse zu optimieren.
Ich möchte gerne 3 verschiedene Postkarten mit Sprüchen von mir gestalten. Postkarten, die man auch verschicken kann und aus denen natürlich meine Kontaktdaten hervorgehen. Mein Logo sollte irgendwo auf der beschreibbaren Seite sichtbar sein. Vorne drauf nur der Spruch und vielleicht eine Zeichnung, eine Karikatur, eine Comiczeichnung oder ein Bild (ich bin offen für alles).
Die Sprüche lauten:
Lieber unperfekt anfangen als gar nicht!
Mach Dir hin und wieder bewusst, wie großartig Du bist!
Frage Dich immer: 'Was ist das Schlimmste, was passieren könnte?' - Es ist selten ein Weltuntergang.
Es sollen drei verschiedene Karten sein, die aber irgendwie zusammenpassen vom Design her.
Meine Hauptzielgruppe, für die auch diese Postkarten hier gedacht sind, sind vor allem Frauen - entweder Frauen, die als Assistentin arbeiten oder selbständig sind.
Aufgabenstellung
Es darf gerne etwas weiblich sein, sollte aber nicht zu bunt und schnörkelig sein. Es darf gerne auffallen. Achtung: Mein Logo sollte ohne Untertitel verwendet werden. Also nur 'Meike Varlow' - ohne 'Training & Coaching'.

```html
<!DOCTYPE html>
<html lang="de">
<head>
<meta charset="utf-8">
<title>Meike Varlow – Postkarte „Lieber unperfekt anfangen“</title>
<link rel="stylesheet" href="https://fonts.googleapis.com/css2?family=Special+Elite&family=Open+Sans:wght@400&display=swap">
<style>
  :root {
    --bg: #dadada;
    --paper: #ffffff;
    --green: #86bc2f;
    --green-faint: #e6f0d6;
    --grey: #5d626b;
    --rule: #b9bcc1;
    --display: "Special Elite", serif;
    --body: "Open Sans", sans-serif;
  }
  * { box-sizing: border-box; margin: 0; padding: 0; }
  html, body { width: 849px; height: 1200px; overflow: hidden; }
  body { background: var(--bg); position: relative; font-family: var(--body); }

  .card { position: absolute; background: var(--paper); box-shadow: 1px 2px 3px rgba(0,0,0,.25); }

  /* Vorderseite */
  .card--front { left: 91px; top: 60px; width: 424px; height: 598px; }
  .front__illustration {
    position: absolute; left: 162px; top: 68px; width: 100px; height: 118px;
    background: radial-gradient(circle, #cfe5ab 0%, #eef6e2 60%, var(--paper) 100%);
    border-radius: 50%;
  }
  .quote { position: absolute; left: 0; right: 0; top: 200px; text-align: center; font-family: var(--display); line-height: 1; }
  .quote__line { display: block; }
  .quote__line--lead { color: var(--grey); font-size: 80px; letter-spacing: 1px; }
  .quote__line--accent { color: var(--green); font-size: 66px; margin-top: -4px; }
  .quote__line--caps { color: var(--green); font-size: 58px; margin-top: 4px; }
  .quote__line--tail { color: var(--grey); font-size: 50px; margin-top: 6px; }

  .front__signoff { position: absolute; left: 0; right: 0; top: 512px; display: flex; align-items: center; justify-content: center; gap: 12px; }
  .front__signoff-rule { width: 44px; height: 2px; background: var(--grey); }
  .front__signoff-name { font-family: var(--display); font-size: 12px; color: var(--green); }

  /* Rückseite */
  .card--back { left: 150px; top: 712px; width: 640px; height: 423px; }
  .sender { position: absolute; left: 70px; top: 34px; }
  .sender__name { font-family: var(--display); font-size: 26px; color: var(--green); display: flex; align-items: center; gap: 8px; }
  .sender__dot { width: 14px; height: 14px; border-radius: 50%; background: var(--grey); }
  .sender__address { margin-top: 6px; font-size: 10px; line-height: 1.35; color: var(--grey); }

  .back__illustration {
    position: absolute; left: 80px; top: 130px; width: 200px; height: 250px;
    background: radial-gradient(ellipse, var(--green-faint) 0%, #f4f8ec 55%, var(--paper) 100%);
    border-radius: 50%;
  }
  .back__divider { position: absolute; left: 316px; top: 160px; width: 2px; height: 200px; background: var(--grey); }
  .address-lines { position: absolute; left: 352px; top: 200px; width: 240px; }
  .address-lines__line { height: 40px; border-bottom: 1px dotted var(--rule); }
</style>
</head>
<body>

  <section class="card card--front" aria-label="Vorderseite">
    <div class="front__illustration" role="img" aria-label="Gezeichnete grüne Rakete mit Strahlen"></div>
    <h1 class="quote">
      <span class="quote__line quote__line--lead">Lieber</span>
      <span class="quote__line quote__line--accent">unperfekt</span>
      <span class="quote__line quote__line--caps">ANFANGEN</span>
      <span class="quote__line quote__line--tail">als gar nicht!</span>
    </h1>
    <div class="front__signoff">
      <span class="front__signoff-rule"></span>
      <span class="front__signoff-name">Meike Varlow</span>
      <span class="front__signoff-rule"></span>
    </div>
  </section>

  <section class="card card--back" aria-label="Rückseite">
    <div class="sender">
      <div class="sender__name"><span class="sender__dot"></span>Meike Varlow</div>
      <p class="sender__address">Lindenweg 12 · 70999 Talhausen<br>T +49 (0)7000 5550123 · meike-varlow.de</p>
    </div>
    <div class="back__illustration" role="img" aria-label="Blasse gezeichnete Rakete mit Strahlen als Hintergrundmotiv"></div>
    <div class="back__divider"></div>
    <div class="address-lines">
      <div class="address-lines__line"></div>
      <div class="address-lines__line"></div>
      <div class="address-lines__line"></div>
      <div class="address-lines__line"></div>
    </div>
  </section>

</body>
</html>
```